Fernbrook Dwellings Business Card Design Project

Please create a custom Business Card Design for Fernbrook Dwellings. The logo is attached to this brief.Please include space for
Name Surname
Title (Solutions Specialist)
Phone
Email
Website
Industry/Entity Type
Business
Contact Information for Business Card
Reverse should be printed horizontally and have the following components:
Small version of the logo. (lowest priority)
The words "Real Estate Solutions Company"
A bulleted list (Note: Line breaks are suggestions only):
* BUY, RENOVATE, SELL and RENT:
RESIDENTIAL PROPERTIES
* MAKE CASH OFFERS ON HOUSES IN
ANY CONDITION and IN ANY SITUATION
* SELL PROPERTIES TO INVESTORS
* SOLVE COMPLEX REAL ESTATE
PROBLEMS and TITLE ISSUES
* PRIVATE MONEY INVESTMENT SERVICES
* PAY CASH REWARDS FOR REFERRALS
Included somewhere on the reverse should also be the following:
Office: (425) 555-0183
www.FernbrookDwellings.example
space for civic trade registry logo
Look and feel
Each slider illustrates characteristics of the customer's brand and the style your logo design should communicate.

```html
<!DOCTYPE html>
<html lang="en">
<head>
<meta charset="utf-8">
<title>Fernbrook Dwellings – Business Card</title>
<link rel="stylesheet" href="https://fonts.googleapis.com/css2?family=Montserrat:wght@600;700&family=Open+Sans:wght@400;600&display=swap">
<style>
  :root {
    --backdrop: #ece8e1;
    --card-white: #f7f8f8;
    --brand-blue: #0f5a86;
    --brand-blue-deep: #0a4468;
    --brand-blue-light: #2f86bd;
    --leaf-green: #7cc242;
    --sun-yellow: #f4d21c;
    --name-green: #b8e04a;
    --text-light: #e6f0f7;
  }
  * { margin: 0; padding: 0; box-sizing: border-box; }
  html, body { width: 1200px; height: 922px; overflow: hidden; }
  body {
    background: var(--backdrop);
    position: relative;
    font-family: "Open Sans", sans-serif;
  }
  .card {
    position: absolute;
    width: 560px;
    height: 320px;
    border-radius: 6px;
    overflow: hidden;
    box-shadow: 0 6px 18px rgba(0,0,0,0.18);
  }
  .card-front { left: 70px; top: 120px; background: var(--card-white); }
  .card-back  { left: 570px; top: 482px; background: linear-gradient(160deg, var(--brand-blue-light) 0%, var(--brand-blue) 45%, var(--brand-blue-deep) 100%); }

  .front-wave, .back-curves { position: absolute; inset: 0; width: 100%; height: 100%; }

  .wordmark {
    position: absolute;
    font-family: "Montserrat", sans-serif;
    font-weight: 700;
    letter-spacing: 1px;
    line-height: 1.1;
    display: flex; align-items: center;
  }
  .front-wordmark {
    left: 34px; top: 128px; width: 220px;
    color: var(--brand-blue-light);
    font-size: 30px;
    gap: 12px;
  }
  .wordmark-dot {
    flex: none;
    width: 38px; height: 38px;
    border-radius: 50%;
    background: var(--sun-yellow);
  }

  .contact {
    position: absolute;
    left: 312px; top: 44px;
    color: var(--text-light);
  }
  .contact-name {
    font-family: "Montserrat", sans-serif;
    font-weight: 700;
    font-size: 22px;
    color: var(--name-green);
  }
  .contact-title {
    font-size: 13px;
    color: var(--name-green);
    margin-bottom: 28px;
  }
  .contact-list { list-style: none; font-size: 11px; }
  .contact-list li { display: flex; align-items: center; gap: 9px; margin-bottom: 13px; white-space: nowrap; }
  .contact-icon {
    width: 16px; height: 16px; border-radius: 3px;
    background: var(--leaf-green);
    display: flex; align-items: center; justify-content: center;
    flex: none;
  }
  .contact-icon svg { width: 10px; height: 10px; }

  .back-content {
    position: absolute; inset: 0;
    padding: 22px 30px;
    color: var(--text-light);
  }
  .back-wordmark {
    position: static;
    color: #ffffff;
    font-size: 22px;
    gap: 10px;
  }
  .back-wordmark .wordmark-dot { width: 26px; height: 26px; }
  .tagline {
    margin-top: 12px;
    font-family: "Montserrat", sans-serif;
    font-weight: 600;
    font-size: 15px;
    color: var(--name-green);
    letter-spacing: 0.5px;
  }
  .services {
    margin-top: 10px;
    list-style: none;
    font-size: 10.5px;
    line-height: 1.45;
  }
  .services li { position: relative; padding-left: 14px; margin-bottom: 2px; }
  .services li::before {
    content: ""; position: absolute; left: 0; top: 5px;
    width: 6px; height: 6px; border-radius: 50%;
    background: var(--sun-yellow);
  }
  .back-footer {
    position: absolute; left: 30px; right: 30px; bottom: 20px;
    display: flex; align-items: flex-end; justify-content: space-between;
    font-size: 12px;
  }
  .back-footer p { line-height: 1.5; }
  .office-label { font-weight: 600; color: var(--name-green); }
  .registry-badge {
    width: 44px; height: 44px; border-radius: 4px;
    background: rgba(255,255,255,0.85);
  }
</style>
</head>
<body>

<section class="card card-front" aria-label="Card front">
  <svg class="front-wave" viewBox="0 0 560 320" preserveAspectRatio="none" aria-hidden="true">
    <path d="M300 0 C250 90 330 170 260 320 L560 320 L560 0 Z" fill="var(--leaf-green)"/>
    <path d="M308 0 C258 90 338 170 270 320 L560 320 L560 0 Z" fill="var(--brand-blue)"/>
  </svg>

  <div class="wordmark front-wordmark">
    <span class="wordmark-dot"></span>
    <span>Fernbrook Dwellings</span>
  </div>

  <div class="contact">
    <p class="contact-name">Name Surname</p>
    <p class="contact-title">Your Position</p>
    <ul class="contact-list">
      <li><span class="contact-icon"><svg viewBox="0 0 10 10"><path d="M2 1 L4 1 L4.5 3 L3.5 4 C4 5.5 4.5 6 6 6.5 L7 5.5 L9 6 L9 8 C5 9 1 5 2 1 Z" fill="#fff"/></svg></span>0123 456 789</li>
      <li><span class="contact-icon"><svg viewBox="0 0 10 10"><rect x="3" y="1" width="4" height="8" rx="0.8" fill="none" stroke="#fff" stroke-width="1"/></svg></span>0123 456 789</li>
      <li><span class="contact-icon"><svg viewBox="0 0 10 10"><rect x="1" y="2.5" width="8" height="5.5" fill="none" stroke="#fff" stroke-width="1"/><path d="M1 2.5 L5 6 L9 2.5" fill="none" stroke="#fff" stroke-width="1"/></svg></span>Yourmail@FernbrookDwellings.example</li>
      <li><span class="contact-icon"><svg viewBox="0 0 10 10"><circle cx="5" cy="5" r="3.8" fill="none" stroke="#fff" stroke-width="1"/><path d="M1.2 5 H8.8 M5 1.2 V8.8" stroke="#fff" stroke-width="0.8"/></svg></span>www.FernbrookDwellings.example</li>
    </ul>
  </div>
</section>

<section class="card card-back" aria-label="Card back">
  <svg class="back-curves" viewBox="0 0 560 320" preserveAspectRatio="none" aria-hidden="true">
    <path d="M0 250 C160 180 300 330 560 220" fill="none" stroke="rgba(255,255,255,0.06)" stroke-width="40"/>
  </svg>
  <div class="back-content">
    <div class="wordmark back-wordmark">
      <span class="wordmark-dot"></span>
      <span>Fernbrook Dwellings</span>
    </div>
    <p class="tagline">Real Estate Solutions Company</p>
    <ul class="services">
      <li>BUY, RENOVATE, SELL and RENT: RESIDENTIAL PROPERTIES</li>
      <li>MAKE CASH OFFERS ON HOUSES IN ANY CONDITION and IN ANY SITUATION</li>
      <li>SELL PROPERTIES TO INVESTORS</li>
      <li>SOLVE COMPLEX REAL ESTATE PROBLEMS and TITLE ISSUES</li>
      <li>PRIVATE MONEY INVESTMENT SERVICES</li>
      <li>PAY CASH REWARDS FOR REFERRALS</li>
    </ul>
    <div class="back-footer">
      <div>
        <p><span class="office-label">Office:</span> (425) 555-0183</p>
        <p>www.FernbrookDwellings.example</p>
      </div>
      <span class="registry-badge" role="img" aria-label="Civic trade registry badge space"></span>
    </div>
  </div>
</section>

</body>
</html>
```